It is a leisure sector investment company.The company plans to invest in a luxurious 5 star resort

We need a stationery design to our company 'Copper Lantern Limited' using the winning logo design. We need the letter heads, envelopes & the business cards. Should be simple, plain and professional
We have upload the source file & vector files which gives our logo design. We prefer the bottom logo.

Have updated under 'must have priorities', the company name, address, tel no. fax no. & the company reg no. which should come on the letter head. the long envelope should have the company name, tel & fax no. 
Business card should have the company name, name on the card, designation, tel no. fax no.  

- Letter head details:
Copper Lantern Limited
14 Floor, South Wing, Halvard Merchant Plaza,
Merrow Court, Colombo 01, Sri Lanka
Tel: +94 11 5047293 Fax: +94 11 5047298
Company Reg No.QX 6142
Long Envelope should have only the company name, adress, Tel & Fax
Business Cards should have the company name, Tel & Fax:
Business Card 1 - Lasantha Gunaratne - Chairman
Business Card 2 - Nimal.T.Wijesooriya - COO

```html
<!DOCTYPE html>
<html lang="en">
<head>
<meta charset="utf-8">
<title>Copper Lantern Limited – Letterhead</title>
<link rel="stylesheet" href="https://fonts.googleapis.com/css2?family=Cinzel:wght@400&family=Arimo:wght@400&display=swap">
<style>
  :root {
    --paper: #ffffff;
    --band-light: #f3f2f1;
    --band-mid: #c9c3c0;
    --band-dark: #857b77;
    --brand-ink: #4b413d;
    --contact-ink: #ffffff;
    --ornament-tint: #efefef;
  }
  html, body {
    margin: 0;
    padding: 0;
    background: var(--paper);
    overflow: hidden;
  }
  .letterhead {
    position: relative;
    width: 927px;
    height: 1200px;
    background: var(--paper);
    overflow: hidden;
  }
  .header-band {
    position: absolute;
    left: 0;
    top: 27px;
    width: 927px;
    height: 159px;
    background: linear-gradient(90deg, var(--band-light) 0%, var(--band-mid) 40%, var(--band-dark) 100%);
  }
  .brand-name {
    position: absolute;
    left: 46px;
    top: 82px;
    width: 270px;
    margin: 0;
    font-family: "Cinzel", "Times New Roman", serif;
    font-weight: 400;
    font-size: 27px;
    line-height: 1.15;
    letter-spacing: 0.5px;
    color: var(--brand-ink);
    text-align: center;
  }
  .contact-block {
    position: absolute;
    right: 55px;
    top: 67px;
    margin: 0;
    font-family: "Arimo", "Helvetica Neue", Arial, sans-serif;
    font-size: 13.5px;
    line-height: 17px;
    color: var(--contact-ink);
    text-align: right;
    font-style: normal;
  }
  .contact-block p {
    margin: 0;
  }
  .contact-block .address {
    margin-bottom: 14px;
  }
  .contact-block .divider {
    display: inline-block;
    margin: 0 4px;
  }
  .ornament-area {
    position: absolute;
    left: 309px;
    top: 778px;
    width: 618px;
    height: 422px;
    background: radial-gradient(ellipse at 65% 60%, var(--ornament-tint) 0%, rgba(239,239,239,0.6) 45%, rgba(255,255,255,0) 75%);
  }
</style>
</head>
<body>
  <main class="letterhead">
    <header class="header-band">
    </header>
    <h1 class="brand-name">Copper Lantern Limited</h1>
    <address class="contact-block">
      <p class="address">14 Floor, South Wing, Halvard Merchant Plaza,<br>Merrow Court, Colombo 01, Sri Lanka</p>
      <p>Tel: +94 11 5047293<span class="divider">|</span>Fax: +94 11 5047298</p>
      <p>Company Reg No. QX 6142</p>
    </address>
    <div class="ornament-area" role="img" aria-label="Large faint decorative flourish in pale grey"></div>
  </main>
</body>
</html>
```